Yard sign

I want it to look similar to this one,

change name to DRAVEK and submit new ideas

Also would like to improvise a bit. let's not make exactly the same thing

would like to change to: Connecticut #1 Company

also change phone to 203-555-0147
and website to
dravekllc.com

this is yard sign. size is 24' Width and 32' Height

Target Market(s)

Roof

Industry/Entity Type

Roofing

Requirements
Must have
• similar colors or add something new

```html
<!DOCTYPE html>
<html lang="en">
<head>
<meta charset="utf-8">
<title>DRAVEK Yard Sign</title>
<link rel="stylesheet" href="https://fonts.googleapis.com/css2?family=Montserrat:wght@600;700;800;900&display=swap">
<style>
  :root {
    --sign-red: #fe0000;
    --sign-yellow: #ffe800;
    --sign-black: #000000;
    --sign-white: #ffffff;
    --backdrop: #ececec;
  }
  * { margin: 0; padding: 0; box-sizing: border-box; }
  html, body {
    width: 1040px;
    height: 1200px;
    overflow: hidden;
    background: var(--backdrop);
    font-family: "Montserrat", sans-serif;
  }
  .yard-sign {
    position: absolute;
    left: 100px;
    top: 40px;
    width: 840px;
    height: 1120px;
    overflow: hidden;
    background: var(--sign-red);
  }
  .sign-bands {
    position: absolute;
    inset: 0;
    width: 840px;
    height: 1120px;
  }
  .headline {
    position: absolute;
    left: 66px;
    top: 110px;
    transform: rotate(-7deg);
    transform-origin: left bottom;
    white-space: nowrap;
  }
  .headline-top {
    display: flex;
    align-items: baseline;
    gap: 22px;
    line-height: 1;
  }
  .headline-state {
    font-size: 66px;
    font-weight: 700;
    color: var(--sign-yellow);
  }
  .headline-rank {
    font-size: 128px;
    font-weight: 900;
    letter-spacing: -4px;
    color: var(--sign-white);
  }
  .headline-word {
    margin-top: 8px;
    font-size: 122px;
    font-weight: 900;
    line-height: 1;
    letter-spacing: -3px;
    color: var(--sign-black);
    text-shadow:
      3px 0 0 var(--sign-white), -3px 0 0 var(--sign-white),
      0 3px 0 var(--sign-white), 0 -3px 0 var(--sign-white),
      3px 3px 0 var(--sign-white), -3px -3px 0 var(--sign-white),
      3px -3px 0 var(--sign-white), -3px 3px 0 var(--sign-white),
      8px 6px 0 var(--sign-yellow);
  }
  .brand-name {
    position: absolute;
    left: 0;
    right: 0;
    top: 708px;
    text-align: center;
    font-size: 166px;
    font-weight: 900;
    line-height: 1;
    letter-spacing: -2px;
    color: var(--sign-red);
    text-shadow:
      3px 0 0 var(--sign-white), -3px 0 0 var(--sign-white),
      0 3px 0 var(--sign-white), 0 -3px 0 var(--sign-white),
      3px 3px 0 var(--sign-white), -3px -3px 0 var(--sign-white),
      3px -3px 0 var(--sign-white), -3px 3px 0 var(--sign-white);
  }
  .phone-bar {
    position: absolute;
    left: 79px;
    top: 876px;
    width: 682px;
    height: 105px;
    background: var(--sign-yellow);
    display: flex;
    align-items: center;
    justify-content: center;
    font-size: 86px;
    font-weight: 800;
    letter-spacing: -1px;
    color: var(--sign-black);
  }
  .web-line {
    position: absolute;
    left: 84px;
    right: 84px;
    top: 1020px;
    display: flex;
    align-items: center;
    justify-content: space-between;
    color: var(--sign-white);
    font-size: 48px;
    font-weight: 600;
    letter-spacing: 5px;
  }
  .web-rule {
    width: 97px;
    height: 2px;
    background: var(--sign-yellow);
  }
</style>
</head>
<body>
  <div class="yard-sign">
    <svg class="sign-bands" viewBox="0 0 695 926" preserveAspectRatio="none" aria-hidden="true">
      <path class="swoosh-yellow" d="M0 432 Q330 575 695 322 L695 362 Q370 610 0 510 Z" fill="#ffe800"/>
      <path class="swoosh-edge" d="M0 432 Q330 575 695 322" fill="none" stroke="#ffffff" stroke-width="2"/>
      <path class="lower-panel" d="M0 510 Q370 610 695 362 L695 926 L0 926 Z" fill="#000000"/>
    </svg>

    <div class="headline">
      <div class="headline-top">
        <span class="headline-state">Connecticut</span>
        <span class="headline-rank">#1</span>
      </div>
      <div class="headline-word">COMPANY</div>
    </div>

    <div class="brand-name">DRAVEK</div>
    <div class="phone-bar">203-555-0147</div>
    <div class="web-line">
      <span class="web-rule"></span>
      <span class="web-address">dravekllc.com</span>
      <span class="web-rule"></span>
    </div>
  </div>
</body>
</html>
```